Business Card Design for my Real Estate Investing Company

This is for a Real Estate Investing Company that will be serving the Las Vegas Valley. Id like the following slogan included: "Investing in Our Community" I have attached my logo. You will see the color tones I'm interested in..in my logo. I would like the card to be double-sided with a modern, professional look.
Target Market(s)
Homeowners, banks, real estate industry
Industry/Entity Type
Real Estate
Contact Information for Business Card
name: Dale Pruitt
position: Managing Member
address: 4812 Corvane Pkwy ste 207-300
N. Las Vegas, NV 89517
phone: (702) 555-0143
fax: (702) 555-0187
email: OakridgeHousePurchaser@examplemail.com
web: OakridgeHousePurchasers.example
*At the bottom of the card I would like....
We buy houses for cash....no repairs, no commissions, no fees!
Logo Text
OAKRIDGE HOUSE PURCHASERS "Investing in Our Community"
Font styles to use
Other font styles liked:
- Lora
Requirements
Must have
- On the back of the card, i'd like to have my logo large and the following statements:
- Are you considering selling your home? Want a simple, hassle-free transaction? We can help! We buy houses for cash and can close quickly! No need to do any repairs, no realtor commissions, no closing costs.....and no headaches. Let us help you with your real estate needs...!
Nice to have
- multiple colors 2 two tone on front and back

```html
<!DOCTYPE html>
<html lang="en">
<head>
<meta charset="utf-8">
<title>Oakridge House Purchasers – Business Card</title>
<link rel="stylesheet" href="https://fonts.googleapis.com/css2?family=Lora:ital,wght@0,400;0,700;1,400&family=Arimo:wght@400&display=swap">
<style>
  :root {
    --page: #4a423d;
    --card: #121212;
    --card-edge: #1c1c1c;
    --brand-blue: #1f62b8;
    --slogan-grey: #b4b4b4;
    --ink-light: #f2f2f2;
    --ink-soft: #d6d6d6;
  }
  * { box-sizing: border-box; margin: 0; padding: 0; }
  html, body {
    width: 1200px; height: 780px; overflow: hidden;
    background: var(--page);
  }
  .canvas {
    width: 1200px; height: 780px;
    display: flex; align-items: center; justify-content: center; gap: 44px;
  }
  .card {
    width: 540px; height: 309px;
    background: var(--card);
    border: 1px solid var(--card-edge);
    border-radius: 4px;
    box-shadow: 0 14px 30px rgba(0,0,0,.45);
    position: relative;
    overflow: hidden;
  }
  .brand { display: flex; flex-direction: column; align-items: center; }
  .brand-row { display: flex; align-items: center; gap: 10px; }
  .brand-mark { width: 18px; height: 18px; background: var(--brand-blue); flex: none; }
  .brand-name {
    font-family: "Lora", serif; font-weight: 700;
    color: var(--brand-blue);
    font-size: 26px; letter-spacing: 0.3px; white-space: nowrap;
  }
  .brand-slogan {
    font-family: "Lora", serif; font-style: italic;
    color: var(--slogan-grey);
    font-size: 12px; letter-spacing: 3.5px; margin-top: 8px;
  }

  /* front */
  .card-front .brand { position: absolute; top: 78px; left: 0; right: 0; }
  .front-tagline {
    position: absolute; left: 0; right: 0; top: 196px;
    text-align: center;
    font-family: "Lora", serif; font-size: 16px;
    color: var(--brand-blue);
  }

  /* back */
  .card-back .details {
    position: absolute; right: 22px; top: 36px; width: 400px;
    display: flex; flex-direction: column; align-items: center; text-align: center;
  }
  .card-back .brand-mark { width: 15px; height: 15px; }
  .card-back .brand-name { font-size: 21px; }
  .card-back .brand-slogan { font-size: 10.5px; letter-spacing: 3px; margin-top: 6px; }
  .person-name {
    font-family: "Lora", serif; font-weight: 700;
    color: var(--ink-light); font-size: 22px; margin-top: 14px; line-height: 1.2;
  }
  .person-title {
    font-family: "Lora", serif; color: var(--ink-soft); font-size: 14px; margin-top: 2px;
  }
  .contact-list {
    list-style: none; margin-top: 12px;
    font-family: "Arimo", sans-serif; color: var(--ink-light);
    font-size: 13.5px; line-height: 1.55; white-space: nowrap;
  }
</style>
</head>
<body>
<main class="canvas">
  <section class="card card-front" aria-label="Card front">
    <div class="brand">
      <div class="brand-row">
        <span class="brand-mark"></span>
        <span class="brand-name">OAKRIDGE HOUSE PURCHASERS</span>
      </div>
      <span class="brand-slogan">"Investing in Our Community"</span>
    </div>
    <p class="front-tagline">We buy houses for cash....no repairs, no commissions, no fees!</p>
  </section>

  <section class="card card-back" aria-label="Card back">
    <div class="details">
      <div class="brand">
        <div class="brand-row">
          <span class="brand-mark"></span>
          <span class="brand-name">OAKRIDGE HOUSE PURCHASERS</span>
        </div>
        <span class="brand-slogan">"Investing in Our Community"</span>
      </div>
      <h1 class="person-name">Dale Pruitt</h1>
      <p class="person-title">Managing Member</p>
      <ul class="contact-list">
        <li>(702) 555-0143</li>
        <li>(702) 555-0187</li>
        <li>OakridgeHousePurchaser@examplemail.com</li>
        <li>OakridgeHousePurchasers.example</li>
        <li>4812 Corvane Pkwy ste 207-300 N. Las Vegas, NV 89517</li>
      </ul>
    </div>
  </section>
</main>
</body>
</html>
```